WP website design (Brenmoor)

We need a wordpress design for an established auction and real estate company based in Kentucky. The winning design will incorporate a professional color scheme with company logo in a clean layout with specified widgets. The design needs to consider that this will be developed on a responsive theme. Color is #307d84, with gray/black or other as an accent/highlight color.

Industry/Entity Type

Real Estate

Requirements
Must have
• Elelments of design need to consider that this site is going to be developed on a responsive theme.

Navigation:
1) Home 2) Current Auctions 3) Past Auctions 4) Meet the Staff 5) For Sellers 6) For Buyers 7) Testimonials 8) Contact Us

Colors will be the blue of logo plus black/gray or other accent color.

Slideshow will be prominent, please use stock real estate photo for initial image. Will have following in either header or sidebar: testimonials, social icons (FB, linkedin Twitter, RSS), Featured Auctions widget, newsletter signup form.

Footer will have contact info (below) and attached affiliation logos.
Brenmoor Auctions, Inc.
8415 Tamsen Rd., Louisville KY 40291
glen.office@brenmoorbid.example
Phone: (502) 736 2048

```html
<!DOCTYPE html>
<html lang="en">
<head>
<meta charset="utf-8">
<title>Brenmoor Auctions, Inc.</title>
<link href="https://fonts.googleapis.com/css2?family=Arimo:ital,wght@0,400;0,700;1,400&display=swap" rel="stylesheet">
<style>
:root{
  --teal:#307d84;
  --teal-dark:#24636a;
  --gold:#f2b51c;
  --gold-light:#f8cf52;
  --ink:#222;
  --gray-text:#555;
  --page-bg:#e6e7e8;
  --panel:#fff;
  --dark-bar:#2b2b2b;
  --footer:#2e2e2e;
  --rule:#d4d4d4;
}
*{box-sizing:border-box;margin:0;padding:0}
html,body{width:874px;height:1200px;overflow:hidden}
body{font-family:"Arimo",Arial,sans-serif;background:var(--page-bg);color:var(--ink);position:relative}
.site-header{position:absolute;left:0;top:0;width:874px;height:92px;background:linear-gradient(#fafafa,#ececec)}
.brand{position:absolute;left:76px;top:24px;display:flex;align-items:center;gap:10px}
.brand-mark{width:34px;height:34px;background:var(--teal)}
.brand-name{font-size:26px;font-weight:700;color:var(--teal)}
.social{position:absolute;right:58px;top:34px;display:flex;gap:8px}
.social span{width:28px;height:28px;border-radius:50%;background:var(--teal)}
.main-nav{position:absolute;left:52px;top:94px;width:772px;height:28px;background:var(--teal);display:flex}
.main-nav a{color:#fff;text-decoration:none;font-size:11px;font-weight:700;line-height:28px;padding:0 16px}
.main-nav a.current{background:var(--gold);color:var(--ink)}
.gold-band{position:absolute;left:0;top:380px;width:874px;height:235px;background:var(--gold)}
.hero{position:absolute;left:52px;top:122px;width:772px;height:422px;background:linear-gradient(#6fa3d8 0%,#a9cbea 40%,#9aa57e 70%,#5e7a3e 100%)}
.content{position:absolute;left:52px;top:544px;width:772px;height:564px;background:var(--page-bg)}
.section-bar{position:absolute;left:26px;width:488px;height:28px;background:var(--teal);color:#fff;font-size:11px;font-weight:700;line-height:28px;padding-left:12px}
.auction-card{position:absolute;left:26px;width:488px;background:var(--panel);border:1px solid var(--rule);padding:16px}
.thumb{position:absolute;left:16px;top:16px;width:86px;height:58px;background:linear-gradient(#8bb6e0,#b5a98f 60%,#6d8a4a)}
.thumb-btn{position:absolute;left:16px;width:86px;height:18px;background:var(--dark-bar);color:#fff;font-size:9px;line-height:18px;padding-left:28px}
.thumb-btn::before{content:"";position:absolute;left:8px;top:5px;width:10px;height:8px;background:#fff}
.card-body{margin-left:100px}
.card-title{font-size:14px;font-weight:700;margin-bottom:6px}
.card-text{font-size:9px;color:var(--gray-text);line-height:1.35;margin-bottom:10px}
.bid-box{background:#f1f1f1;border:1px solid var(--rule);padding:8px 10px;font-size:9px;line-height:1.45}
.bid-box strong{font-size:10px}
.bid-btn{display:inline-flex;align-items:center;gap:6px;background:var(--gold);color:var(--ink);font-weight:700;font-size:9px;padding:3px 10px 3px 6px;margin:4px 0 6px}
.bid-btn i{width:10px;height:10px;background:var(--ink);display:inline-block}
.sidebar{position:absolute;left:545px;width:227px}
.side-head{background:var(--dark-bar);color:#fff;font-size:14px;font-weight:700;height:30px;line-height:30px;padding-left:10px}
.side-box{background:var(--panel);border:1px solid var(--rule);padding:10px;font-size:9px;color:var(--gray-text);line-height:1.4}
.signup{display:flex;margin-top:8px}
.signup input{width:150px;height:20px;border:1px solid #bbb;font:9px "Arimo",Arial,sans-serif;padding:0 4px}
.signup button{width:30px;height:20px;margin-left:6px;border:0;background:var(--teal);color:#fff;font:700 10px "Arimo",Arial,sans-serif}
.feature-photo{width:100%;height:78px;margin:6px 0;background:linear-gradient(#8bb6e0,#c4b79c 60%,#6d8a4a)}
.testimonial{font-style:italic}
.testimonial-name{text-align:right;margin-top:6px;color:var(--teal)}
.site-footer{position:absolute;left:52px;top:1108px;width:772px;height:74px;background:var(--footer);color:#ddd;font-size:9px;line-height:1.45;padding:10px 14px}
.site-footer strong{color:#fff}
.badges{position:absolute;right:16px;top:24px;display:flex;gap:10px}
.badges span{width:40px;height:28px;background:#cfcfcf}
.copyright{position:absolute;left:52px;top:1182px;width:772px;height:18px;background:#1e1e1e;color:#999;font-size:8px;text-align:center;line-height:18px}
</style>
</head>
<body>
<header class="site-header">
  <div class="brand"><span class="brand-mark"></span><span class="brand-name">Brenmoor Auctions, Inc.</span></div>
  <div class="social" aria-label="Social links"><span></span><span></span><span></span><span></span></div>
</header>
<nav class="main-nav">
  <a href="#">Home</a><a class="current" href="#">Current Auctions</a><a href="#">Past Auctions</a><a href="#">Meet the Staff</a><a href="#">For Sellers</a><a href="#">For Buyers</a><a href="#">Testimonials</a><a href="#">Contact Us</a>
</nav>
<div class="gold-band"></div>
<div class="hero" role="img" aria-label="Slideshow photo of a two-storey family house with a lawn and trees under a blue sky"></div>

<main class="content">
  <div class="section-bar" style="top:74px">Lorem Ipsum has been the industry's standard dummy text ever since the</div>
  <article class="auction-card" style="top:110px;height:206px">
    <div class="thumb" role="img" aria-label="Auction property photo"></div>
    <div class="thumb-btn" style="top:80px">Details</div>
    <div class="thumb-btn" style="top:102px">Video</div>
    <div class="card-body">
      <h2 class="card-title">This is a test of the Lantern Auction System.</h2>
      <p class="card-text">This is a test auction, for the purpose of design and functionality testing of the bidding system. This is a test, for the purpose of design and testing only.</p>
      <div class="bid-box">
        <strong>Live On-Site Auction with Online Bidding</strong><br>
        Begins: Monday, June 20, 2022 at 1:00 PM EDT<br>
        <span class="bid-btn"><i></i>Click Here to Bid Online Now!</span><br>
        Location:<br>P.O. Box 41172<br>Bardstown, KY 40004
      </div>
    </div>
  </article>

  <div class="section-bar" style="top:342px">Lorem Ipsum has been the industry's standard dummy text ever since the</div>
  <article class="auction-card" style="top:378px;height:168px">
    <div class="thumb" role="img" aria-label="Auction property photo"></div>
    <div class="thumb-btn" style="top:80px">Details</div>
    <div class="thumb-btn" style="top:102px">Video</div>
    <div class="card-body">
      <h2 class="card-title">This is a test of the Lantern Auction System.</h2>
      <p class="card-text">This is a test auction, for the purpose of design and functionality testing of the bidding system. This is a test, for the purpose of design and testing only.</p>
      <div class="bid-box">
        <strong>Live On-Site Auction with Online Bidding</strong><br>
        Begins: Thursday, June 30, 2022 at 1:00 PM EDT<br>
        <span class="bid-btn"><i></i>Click Here to Bid Online Now!</span><br>
        Location: P.O. Box 41172, Bardstown, KY 40004
      </div>
    </div>
  </article>

  <aside class="sidebar" style="top:74px">
    <div class="side-head">Sign Up for newsletter</div>
    <div class="side-box">
      Enter your email address to receive auction alerts
      <div class="signup"><input type="text" placeholder="Enter your email address"><button>Go</button></div>
    </div>
    <div class="side-head" style="margin-top:14px">Featured Auction</div>
    <div class="side-box">
      Test Auction Hide
      <div class="feature-photo" role="img" aria-label="Featured auction house photo"></div>
      10/23/16 at 1:00 PM ET<br>Middle Cocktail Ln<br>Bardstown, KY 40004
    </div>
    <div class="side-head" style="margin-top:14px">Clients Testimonials</div>
    <div class="side-box">
      <p class="testimonial">Bidding with this team was easy from start to finish. They sold our family farm for more than we hoped and kept us informed every step of the way. We would gladly work with them again and recommend them to anyone selling property.</p>
      <p class="testimonial-name">Dana Whitfield</p>
    </div>
  </aside>
</main>

<footer class="site-footer">
  <strong>Brenmoor Auctions, Inc.</strong><br>
  8415 Tamsen Rd., Louisville KY 40291<br>
  glen.office@brenmoorbid.example<br>
  Phone: (502) 736 2048
  <div class="badges" aria-label="Affiliations"><span></span><span></span><span></span><span></span></div>
</footer>
<div class="copyright">Copyright (c) Brenmoor Auctions 2014-2016. All Rights Reserved</div>
</body>
</html>
```